Women's Online Clothing Boutique Needs Business Cards

I already have a logo that I would like to use. Some of the things that interest me is black business cards, foil embossed logo, glossy embossed logo, leopard print, no yellow font, rounded edges. I even like just a large logo on the front side with all of my information on the back side.

Contact Information for Business Card

https://silverheron.shopvenlo.com/
https://www.pagelink.net/thesilverheronboutique/
https://www.picfeed.net/thesilverheronboutique/
silverheronboutique@mailora.net

Requirements
Must have
• My Logo
Nice to have
• Leopard Print
Should not have
• No Yellow Font

```html
<!DOCTYPE html>
<html lang="en">
<head>
<meta charset="utf-8">
<title>The Silver Heron Boutique – Business Card</title>
<link href="https://fonts.googleapis.com/css2?family=Questrial&display=swap" rel="stylesheet">
<style>
  :root {
    --backdrop: #a9abaf;
    --card-black: #1b1b1a;
    --card-charcoal: #393939;
    --ink-white: #f4f4f2;
    --rule-white: #f1f1f1;
  }
  * { box-sizing: border-box; margin: 0; padding: 0; }
  html, body {
    width: 1200px; height: 857px; overflow: hidden;
    background: var(--backdrop);
    font-family: "Questrial", "Century Gothic", sans-serif;
    color: var(--ink-white);
  }
  .sheet {
    width: 1200px; height: 857px;
    display: flex; align-items: center; justify-content: center; gap: 40px;
  }
  .card {
    width: 520px; height: 297px;
    border-radius: 12px;
    overflow: hidden;
    box-shadow: 0 10px 24px rgba(0,0,0,.25);
  }
  /* Front */
  .card-front {
    background: var(--card-black);
    display: flex; align-items: center; justify-content: center;
  }
  .brand-name {
    font-size: 38px; letter-spacing: .5px; line-height: 1.15;
    text-align: center;
  }
  /* Back */
  .card-back {
    background: var(--card-charcoal);
    display: flex; flex-direction: column;
    padding: 26px 0 30px;
  }
  .contact-row {
    display: flex; align-items: center; justify-content: center; gap: 12px;
    flex: 1;
    border-bottom: 4px solid var(--rule-white);
    margin: 0 28px;
  }
  .contact-row:last-child { border-bottom: 4px solid var(--rule-white); }
  .contact-web { font-size: 24px; letter-spacing: .4px; }
  .contact-social { font-size: 21px; letter-spacing: .3px; }
  .contact-mail { font-size: 16px; letter-spacing: .3px; }
  .social-mark {
    width: 24px; height: 24px; border-radius: 5px;
    background: var(--ink-white); flex: none;
  }
</style>
</head>
<body>
  <main class="sheet">
    <section class="card card-front" aria-label="Card front">
      <h1 class="brand-name">The Silver Heron<br>Boutique</h1>
    </section>
    <section class="card card-back" aria-label="Card back">
      <p class="contact-row contact-web">silverheron.shopvenlo.com</p>
      <p class="contact-row contact-social"><span class="social-mark" aria-hidden="true"></span>thesilverheronboutique</p>
      <p class="contact-row contact-social"><span class="social-mark" aria-hidden="true"></span>thesilverheronboutique</p>
      <p class="contact-row contact-mail">silverheronboutique@mailora.net</p>
    </section>
  </main>
</body>
</html>
```